HizliDolum.Net - Mobile Top Up

It is the top up site for mobile operators.

Works for 3 mobile operators; Telvora, Mavicom, Yildiz Iletisim
This site will broadcast in Turkish and English for this reason we want to select the language button.
This site will usually serve for Turkey.
Required Pages;

Home page
Payment Page
Communication Page
About Us

We need a colorful and responsive design. Customer reviews, recharge form, and some information should be included at the homepage.

The payment page should include a credit card payment form and customer information.

We want eye-pleasing designs, innovative and easy to use.
Updates

Dear designers :) Please do not make similar designs to our current design !. We started this contest because we wanted a different design. Logic and design will be a mobile top-up site. You can look at it, but please do not do the same!

Target Market(s)

Top up Website

Logo Text

HizliDolum

Coding

Coded - Design and coding required

Number of Pages Required

4 page

Font styles to use
Serif

Colors
6b449b
e24096
33a6d7
abd036
fbf289
f68d4d
f04a50
d3a5cc

Requirements
Must have
• Payment , contact form, fast payment form , top up form
Nice to have
• look our current design : hizlidolum.net - we want responsive design

```html
<!DOCTYPE html>
<html lang="en">
<head>
<meta charset="utf-8">
<title>HizliDolum.Net – Mobile Top Up</title>
<link href="https://fonts.googleapis.com/css2?family=Open+Sans:wght@400;600;700&family=Roboto+Condensed:wght@400;700&display=swap" rel="stylesheet">
<style>
:root{
  --purple:#6b449b;
  --pink:#e24096;
  --blue:#33a6d7;
  --blue-deep:#1f93d1;
  --green:#8cc63f;
  --green-dark:#76b82a;
  --orange:#f68d4d;
  --red:#f04a50;
  --teal:#2bb3a3;
  --ink:#333a40;
  --text:#5b6168;
  --muted:#8a9097;
  --line:#e4e6e9;
  --soft:#f4f5f7;
  --footer:#f2f3f4;
}
*{margin:0;padding:0;box-sizing:border-box}
html,body{width:1200px;height:2894px;overflow:hidden}
body{position:relative;background:#fff;font-family:"Open Sans",sans-serif;color:var(--text)}
.abs{position:absolute}

/* header */
.brand{left:100px;top:34px;font:700 34px "Open Sans",sans-serif;color:var(--green-dark);display:flex;align-items:center;gap:10px}
.brand .dot{width:22px;height:22px;border-radius:50%;background:var(--blue)}
.lang{right:60px;top:20px;font-size:13px;color:var(--ink);display:flex;gap:12px}
.lang .on{color:var(--blue)}
.nav{right:56px;top:56px;display:flex;gap:30px;font:400 14px "Roboto Condensed",sans-serif;text-transform:uppercase}
.nav a{text-decoration:none;display:flex;align-items:center;gap:8px}
.nav i{width:13px;height:13px;border-radius:3px;display:inline-block}

/* hero */
.hero{left:0;top:100px;width:1200px;height:504px;background:linear-gradient(120deg,#3b4a57 0%,#6e7a82 35%,#b8b2a6 70%,#d9d3c6 100%)}
.hero-box{left:100px;top:212px;width:475px;height:232px;background:rgba(31,147,209,.92);padding:24px 32px}
.hero-box h1{font:700 38px "Roboto Condensed",sans-serif;color:#fff;line-height:1.05}
.hero-box p{font-size:14px;color:#fff;margin-top:4px}
.hero-input{margin-top:24px;height:40px;background:#fff;border-radius:3px;display:flex;align-items:center;padding-left:14px;gap:12px;font-size:13px;color:var(--ink);width:409px}
.btn{display:inline-block;background:var(--green);color:#fff;font:600 15px "Open Sans",sans-serif;border-radius:3px}
.hero-btn{margin-top:14px;padding:10px 22px}
.hero-arrow{left:612px;top:380px}

/* why */
.why-bg{left:0;top:604px;width:1200px;height:428px;background:var(--soft)}
.section-title{font:400 30px "Roboto Condensed",sans-serif;color:var(--ink);text-transform:uppercase;letter-spacing:.5px}
.why-title{left:0;top:714px;width:1200px;display:flex;justify-content:center;align-items:center;gap:34px}
.why-title span.rule{width:110px;height:3px;background:var(--ink)}
.why-copy{left:145px;top:770px;width:910px;font-size:11.5px;line-height:20px;text-align:center}
.why-copy p+p{margin-top:8px}
.op-card{top:932px;width:311px;height:233px;background:#fff;border:1px solid var(--line);text-align:center}
.op-name{height:110px;display:flex;align-items:center;justify-content:center;font:700 28px "Open Sans",sans-serif;color:var(--ink)}
.op-card p{font-size:11.5px;line-height:20px;padding:0 30px}
.op-btn{margin-top:14px;padding:7px 18px;font-size:12px;font-weight:700}

/* steps */
.steps-phone{left:280px;top:1244px;width:225px;height:425px;border-radius:34px;background:linear-gradient(180deg,#f1ede4 0%,#e3ddd0 100%)}
.steps-title{left:577px;top:1270px;font:400 31px "Roboto Condensed",sans-serif;color:var(--ink);line-height:38px;text-transform:uppercase}
.step{left:577px;width:400px;display:flex;gap:22px}
.step .ico{width:70px;height:70px;border:2px solid #cfe7f4;border-radius:50%;display:flex;align-items:center;justify-content:center;flex:none}
.step h3{font:400 19px "Roboto Condensed",sans-serif;color:var(--ink);margin-top:4px}
.step p{font-size:11.5px;line-height:20px;margin-top:6px}

/* secure band */
.secure{left:0;top:1753px;width:1200px;height:388px;background:linear-gradient(110deg,#2e9fdc 0%,#45b0e5 50%,#3aa8e0 100%)}
.secure h2{position:absolute;top:66px;width:1200px;text-align:center;color:#fff;font:400 31px "Roboto Condensed",sans-serif;line-height:38px;text-transform:uppercase}
.secure p{position:absolute;top:156px;left:230px;width:740px;text-align:center;color:#eaf6fd;font-size:12px;line-height:20px}
.badges{position:absolute;top:234px;left:274px;display:flex;gap:22px}
.badge{width:153px;height:69px;background:#fff;display:flex;align-items:center;justify-content:center}
.badge span{display:block;background:#d7dde2}

/* blog */
.blog-title{left:100px;top:2200px}
.blog-nav{left:1072px;top:2206px;display:flex;gap:8px}
.post-img{top:2272px;width:186px;height:164px}
.post{top:2268px;width:260px}
.post h4{font:400 17px "Roboto Condensed",sans-serif;color:var(--ink)}
.tag{display:inline-block;margin-top:16px;background:var(--orange);color:#fff;font-size:11px;padding:4px 10px}
.post p{font-size:11.5px;line-height:20px;margin-top:10px}
.post .more{font-size:12.5px;color:var(--ink);margin-top:8px}

/* footer */
.footer{left:0;top:2533px;width:1200px;height:299px;background:var(--footer)}
.f-brand{left:100px;top:2592px;font:700 28px "Open Sans",sans-serif;color:var(--green-dark);display:flex;align-items:center;gap:8px}
.f-brand .dot{width:18px;height:18px;border-radius:50%;background:var(--blue)}
.f-contact{left:100px;top:2646px;font-size:12.5px;color:var(--ink);line-height:20px}
.f-contact .row{display:flex;gap:14px;margin-bottom:12px}
.f-contact svg{flex:none;margin-top:3px}
.f-head{font:400 17px "Roboto Condensed",sans-serif;color:var(--ink);text-transform:uppercase}
.news{left:440px;top:2585px;width:245px}
.news p{font-size:11.5px;line-height:20px;margin-top:14px}
.news .input{margin-top:14px;height:40px;background:#fff;border:1px solid var(--line);font-size:12px;color:var(--ink);padding:11px 12px}
.news .btn{margin-top:10px;padding:10px 22px;font-size:13px;font-weight:700}
.links{left:787px;top:2580px}
.links ul{list-style:none;margin-top:18px}
.links li{font-size:12px;color:var(--ink);line-height:20.5px;display:flex;align-items:center;gap:12px}
.links li:before{content:"";border-left:5px solid var(--ink);border-top:4px solid transparent;border-bottom:4px solid transparent}
.social{left:1003px;top:2580px}
.social ul{list-style:none;margin-top:18px}
.social li{display:flex;align-items:center;gap:10px;font-size:13px;color:var(--muted);height:36px}
.social li span{width:26px;height:26px;border:1px solid #b9bec3;border-radius:50%}
.bottom{left:0;top:2832px;width:1200px;height:62px;background:#fff;border-top:1px solid var(--line)}
.bottom p{position:absolute;left:100px;top:22px;font-size:11.5px;color:var(--ink)}
.cards{position:absolute;left:935px;top:18px;display:flex;gap:6px}
.cards span{width:38px;height:24px;border-radius:3px;border:1px solid var(--line);background:var(--footer)}
</style>
</head>
<body>

<!-- header -->
<div class="abs brand"><span class="dot"></span>HizliDolum</div>
<div class="abs lang"><span class="on">ENGLISH</span><span>|</span><span>TURKISH</span></div>
<nav class="abs nav">
  <a style="color:var(--purple)"><i style="background:var(--purple)"></i>Home</a>
  <a style="color:var(--green-dark)"><i style="background:var(--green-dark)"></i>About Us</a>
  <a style="color:var(--pink)"><i style="background:var(--pink)"></i>Dealership</a>
  <a style="color:var(--teal)"><i style="background:var(--teal)"></i>Prices</a>
  <a style="color:var(--blue-deep)"><i style="background:var(--blue-deep)"></i>Contact</a>
  <a style="color:var(--red)"><i style="background:var(--red)"></i>Comments</a>
</nav>

<!-- hero -->
<div class="abs hero" role="img" aria-label="Photo of a man using his mobile phone on a street, with a smartphone showing the top-up form"></div>
<div class="abs hero-box">
  <h1>Fast, Easy Installation TL</h1>
  <p>All operators per installation immediately 0 commission.</p>
  <div class="hero-input">
    <svg width="10" height="16" viewBox="0 0 10 16"><rect x="1" y="1" width="8" height="14" rx="1.5" fill="none" stroke="#333a40" stroke-width="1.6"/><circle cx="5" cy="12.5" r="1" fill="#333a40"/></svg>
    +90 500 000 00 00
  </div>
  <span class="btn hero-btn">Download Now</span>
</div>
<svg class="abs hero-arrow" width="110" height="50" viewBox="0 0 110 50"><path d="M4 40 C30 52 70 48 100 18" fill="none" stroke="#fff" stroke-width="3" stroke-linecap="round"/><path d="M88 16 L102 15 L100 30" fill="none" stroke="#fff" stroke-width="3" stroke-linecap="round" stroke-linejoin="round"/></svg>

<!-- why -->
<div class="abs why-bg"></div>
<div class="abs why-title"><span class="rule"></span><h2 class="section-title">Why should you choose us?</h2><span class="rule" style="background:#fff"></span></div>
<div class="abs why-copy">
  <p>One of the conveniences that technology brings is our mobile phone. In today's age 7-24 is an important tool that we do not separate from ourselves. We use our mobile phone when we are on the road, when our money is gone, when we go to a yard, when we need to call someone whenever we need a trip for a job. If you can not find a business place open at 7pm at night at 3pm, yesterday and evening at 11pm, we will not be able to load TL and can not contact anyone.</p>
  <p>We are an open business place for you 7-24. Everything is fully automated and we do not charge you any additional penny commissions. Our company 7-24 responds to your inquiries by supporting you and your transactions are carried out in 100% secure sub-production.</p>
</div>

<div class="abs op-card" style="left:114px">
  <div class="op-name">Mavicom</div>
  <p>10 TL, 20 TL, 25 TL, 30 TL, 50 TL and 100 TL with credit card 7 Days / 24 Hours</p>
  <span class="btn op-btn">LOAD NOW ›</span>
</div>
<div class="abs op-card" style="left:442px">
  <div class="op-name">Yildiz Iletisim</div>
  <p>10 TL, 20 TL, 25 TL, 30 TL, 50 TL and 100 TL with credit card 7 Days / 24 Hours</p>
  <span class="btn op-btn">LOAD NOW ›</span>
</div>
<div class="abs op-card" style="left:772px">
  <div class="op-name">Telvora</div>
  <p>10 TL, 20 TL, 25 TL, 30 TL, 50 TL and 100 TL with credit card 7 Days / 24 Hours</p>
  <span class="btn op-btn">LOAD NOW ›</span>
</div>

<!-- steps -->
<div class="abs steps-phone" role="img" aria-label="Smartphone showing the mobile top-up form"></div>
<h2 class="abs steps-title">Only 3 easy steps you can<br>do the TL upload!</h2>
<div class="abs step" style="top:1382px">
  <div class="ico"><svg width="26" height="26" viewBox="0 0 24 24"><path d="M6.6 10.8c1.4 2.8 3.8 5.1 6.6 6.6l2.2-2.2c.3-.3.7-.4 1-.2 1.1.4 2.3.6 3.6.6.6 0 1 .4 1 1V20c0 .6-.4 1-1 1C10.6 21 3 13.4 3 4c0-.6.4-1 1-1h3.5c.6 0 1 .4 1 1 0 1.3.2 2.5.6 3.6.1.3 0 .7-.2 1z" fill="none" stroke="#1f93d1" stroke-width="1.6"/></svg></div>
  <div><h3>Enter Phone Number</h3><p>Select the operator and enter the phone number of the desired counter.</p></div>
</div>
<div class="abs step" style="top:1478px">
  <div class="ico"><svg width="26" height="26" viewBox="0 0 24 24"><path d="M3 12V4h8l10 10-8 8z" fill="none" stroke="#1f93d1" stroke-width="1.6" stroke-linejoin="round"/><circle cx="7.5" cy="8" r="1.5" fill="#1f93d1"/></svg></div>
  <div><h3>Select Quantity and Payment</h3><p>Choose the amount of TL you want to upload and perform your payment.</p></div>
</div>
<div class="abs step" style="top:1575px">
  <div class="ico"><svg width="26" height="26" viewBox="0 0 24 24"><path d="M12 15V4M7 9l5-5 5 5" fill="none" stroke="#1f93d1" stroke-width="1.8" stroke-linecap="round" stroke-linejoin="round"/><path d="M3 14v6h18v-6" fill="none" stroke="#1f93d1" stroke-width="1.8"/></svg></div>
  <div><h3>TL 7-24 instantly loaded!</h3><p>All in all, you have done your TL uploading process. !</p></div>
</div>

<!-- secure band -->
<section class="abs secure">
  <h2>Safe automatically process completed<br>by process technology.</h2>
  <p>Trading on our site is like a ATM withdrawal, fully automated and a brokerage house bridging between User banks. No transactions are harmed because the transactions you make are transmitted directly to the company by encrypting them.</p>
  <div class="badges">
    <div class="badge"><span style="width:100px;height:36px;border-radius:4px"></span></div>
    <div class="badge"><span style="width:90px;height:36px;border-radius:18px"></span></div>
    <div class="badge"><span style="width:40px;height:40px;border-radius:50%"></span></div>
    <div class="badge"><span style="width:104px;height:22px"></span></div>
  </div>
</section>

<!-- blog -->
<h2 class="abs section-title blog-title">Latest Blog</h2>
<div class="abs blog-nav">
  <svg width="10" height="14" viewBox="0 0 10 14"><path d="M8 1 2 7l6 6" fill="none" stroke="#333a40" stroke-width="2"/></svg>
  <svg width="10" height="14" viewBox="0 0 10 14"><path d="M2 1l6 6-6 6" fill="none" stroke="#333a40" stroke-width="2"/></svg>
</div>
<div class="abs post-img" style="left:100px;background:linear-gradient(135deg,#c9825a 0%,#8a3b2a 55%,#3a2a26 100%)" role="img" aria-label="Blog photo of a woman drinking coffee while looking at her phone"></div>
<article class="abs post" style="left:311px">
  <h4>Nulla at diam ornare, aliquam urna</h4>
  <span class="tag">FEB 25, 2017</span>
  <p>Nulla at diam ornare, aliquam urna vel, commodo urna. Nam id risus a est luctus consectetur quis eget libero. Suspendisse potenti. Pellentesque habitant morbi tristique senectus</p>
  <p class="more">Read More +</p>
</article>
<div class="abs post-img" style="left:629px;background:linear-gradient(135deg,#9fb0bf 0%,#4c5d6e 55%,#2a3440 100%)" role="img" aria-label="Blog photo of a smiling man in a suit holding a phone"></div>
<article class="abs post" style="left:841px">
  <h4>Nulla at diam ornare, aliquam urna</h4>
  <span class="tag">FEB 25, 2017</span>
  <p>Nulla at diam ornare, aliquam urna vel, commodo urna. Nam id risus a est luctus consectetur quis eget libero. Suspendisse potenti. Pellentesque habitant morbi tristique senectus</p>
  <p class="more">Read More +</p>
</article>

<!-- footer -->
<footer class="abs footer"></footer>
<div class="abs f-brand"><span class="dot"></span>HizliDolum</div>
<div class="abs f-contact">
  <div class="row"><svg width="12" height="16" viewBox="0 0 12 16"><path d="M6 15s5-5.5 5-9A5 5 0 0 0 1 6c0 3.5 5 9 5 9z" fill="#333a40"/><circle cx="6" cy="6" r="2" fill="#f2f3f4"/></svg><div>HizliDolum<br>14 Liman Sokak, Izmir 35210</div></div>
  <div class="row"><svg width="13" height="13" viewBox="0 0 24 24"><path d="M6.6 10.8c1.4 2.8 3.8 5.1 6.6 6.6l2.2-2.2c.3-.3.7-.4 1-.2 1.1.4 2.3.6 3.6.6.6 0 1 .4 1 1V20c0 .6-.4 1-1 1C10.6 21 3 13.4 3 4c0-.6.4-1 1-1h3.5c.6 0 1 .4 1 1 0 1.3.2 2.5.6 3.6.1.3 0 .7-.2 1z" fill="#333a40"/></svg><div>Phone: (232) 555-0148</div></div>
  <div class="row"><svg width="13" height="10" viewBox="0 0 13 10"><rect width="13" height="10" rx="1" fill="#333a40"/><path d="M1 1l5.5 4.5L12 1" fill="none" stroke="#f2f3f4" stroke-width="1.2"/></svg><div>Email: info@hizlidolum.net</div></div>
</div>
<div class="abs news">
  <h3 class="f-head">Sign up for newsletter</h3>
  <p>Excepteur sint occaecat cupidatat non proident, sunt in culpa qui officia deserunt</p>
  <div class="input">Enter email</div>
  <span class="btn">SIGN UP</span>
</div>
<div class="abs links">
  <h3 class="f-head">Quick Links</h3>
  <ul><li>Home</li><li>Dealership</li><li>Prices</li><li>about us</li><li>Contact</li><li>Blog</li><li>Customer comments</li></ul>
</div>
<div class="abs social">
  <h3 class="f-head">Social</h3>
  <ul><li><span></span>Friendbook</li><li><span></span>Chirper</li><li><span></span>Circles+</li><li><span></span>Vidtube</li></ul>
</div>
<div class="abs bottom">
  <p>©2017 HizliDolum, All Rights Reserved.</p>
  <div class="cards"><span></span><span></span><span></span><span></span></div>
</div>

</body>
</html>
```